Lanterns Harvest Night flyer design contest

Name of event: Lantern’s Harvest Night

Tagline: ‘While the Queen’s away the staff will play’

Description: ‘…while the Queen is out celebrating her birthday with high tea, the palace staff are throwing a party at 14th loftspace and drinking her booze!

Date: Sunday 10th June 2012

Time: 8pm-3am

Dress code: Smart/casual or join in the theme

TICKETS
-Purchased through our website or Friendlink page, at the venue or at the door

Pre-Purchase Tickets: $10

Entry on the night (subject to availability): $15

Tickets Include:

Priority entry
Finger food from 9-10pm
‘Kir Royal’ cocktail on arrival

DRINK SPECIALS

$10 Kir Royal’s all night long!
$20 Valdoro buckets from 9-11pm

DJ's

Playing from 9-3am

Line up includes:

Dusky Amber
Tilted
DJ Marvek

Ph: (03) 9514 2760
Web: www.14thloftspace.com.au
Address: 14 Marlowe Lane St Kilda

I have attached an image which shows the feel that I am going for (plz see att.)

Reason: I wanted a 3 day deadline but this option was not available on the booking screen

Hi there,

If anyone finds a stock image that is appropriate you can add the low res to the mock up and if your design wins i can purchase the image to replace it (up to $20).. hope this helps :) Lira

Target Market(s)

Target Market is 20-35 year olds

Industry/Entity Type

Apartment

Requirements
Must have
• Must have a graphical/picture element to it
Also must have our company logo
Must have all the information listed in the task description
Must be a fun and cool design

```html
<!DOCTYPE html>
<html lang="en">
<head>
<meta charset="utf-8">
<title>Lantern's Harvest Night – 14th loftspace</title>
<link href="https://fonts.googleapis.com/css2?family=Sniglet:wght@800&family=Kaushan+Script&family=Roboto+Condensed:wght@300;400;700&display=swap" rel="stylesheet">
<style>
  :root {
    --page: #ffffff;
    --frame: #9a9a9a;
    --wine-light: #a8234f;
    --wine: #7a1638;
    --wine-dark: #3f0a1f;
    --gold: #f6d21c;
    --gold-light: #fff6c8;
    --orange: #f39a12;
    --title-edge: #c0161f;
    --white: #ffffff;
    --mist: #d9bcc6;
    --lime: #d5df3a;
    --ink: #111111;
  }
  * { box-sizing: border-box; margin: 0; padding: 0; }
  html, body { width: 1200px; height: 1200px; overflow: hidden; background: var(--page); }
  body { position: relative; font-family: "Roboto Condensed", "Arial Narrow", sans-serif; }

  .flyer {
    position: absolute; left: 185px; top: 12px; width: 831px; height: 1173px;
    border: 1px solid var(--frame); overflow: hidden;
    background: radial-gradient(ellipse 75% 55% at 45% 40%, var(--wine-light) 0%, var(--wine) 50%, var(--wine-dark) 100%);
    color: var(--white);
  }

  .party-photo {
    position: absolute; left: 360px; top: -20px; width: 480px; height: 560px;
    background: radial-gradient(closest-side at 55% 45%, #f1c98a 0%, #c9783a 40%, rgba(160,60,50,0.5) 75%, rgba(122,22,56,0) 100%);
  }
  .crown-art {
    position: absolute; left: 70px; top: 30px; width: 260px; height: 220px;
    background: radial-gradient(closest-side at 50% 50%, #ffd54a 0%, #e0a418 50%, rgba(216,155,18,0.45) 78%, rgba(216,155,18,0) 100%);
  }

  .event-title { position: absolute; left: 0; top: 0; font-family: "Sniglet", "Arial Rounded MT Bold", sans-serif; font-weight: 800; }
  .event-title span {
    position: absolute; white-space: nowrap; line-height: 1;
    background: linear-gradient(180deg, var(--gold-light) 10%, var(--gold) 70%);
    -webkit-background-clip: text; background-clip: text; color: transparent;
    filter: drop-shadow(3px 3px 0 var(--title-edge)) drop-shadow(-1px -1px 0 var(--title-edge));
  }
  .title-line-1 { left: 34px; top: 222px; font-size: 98px; }
  .title-line-2 { left: 96px; top: 327px; font-size: 98px; }
  .event-title .title-line-3 {
    left: 64px; top: 440px; font-size: 66px;
    background: linear-gradient(180deg, #ffd23a, var(--orange));
    -webkit-background-clip: text; background-clip: text;
  }

  .tagline {
    position: absolute; left: 300px; top: 448px; width: 520px;
    font-family: "Kaushan Script", cursive; font-size: 34px; line-height: 1.05;
    transform: rotate(-6deg); transform-origin: left top; text-align: center;
  }

  .intro {
    position: absolute; left: 70px; top: 576px; width: 690px;
    color: var(--gold); font-weight: 700; font-size: 20px; line-height: 1.2;
  }

  .when { position: absolute; left: 70px; top: 638px; display: flex; align-items: flex-start; }
  .date { width: 226px; font-weight: 700; font-size: 72px; line-height: 0.92; letter-spacing: -2px; }
  .date small { font-size: 26px; font-weight: 400; letter-spacing: 0; }
  .date sup { font-size: 28px; vertical-align: 32px; letter-spacing: 0; }
  .time { width: 247px; padding-left: 14px; border-left: 1px solid var(--mist); font-weight: 700; font-size: 72px; line-height: 0.92; letter-spacing: -2px; }
  .time small { font-weight: 300; font-size: 72px; }
  .dress { padding-left: 14px; border-left: 1px solid var(--mist); font-weight: 300; font-size: 27px; line-height: 1.05; color: var(--mist); }
  .dress strong { display: block; font-weight: 400; font-size: 31px; color: var(--white); }

  .heading { color: var(--gold); font-size: 17px; font-weight: 400; text-transform: uppercase; line-height: 1.25; }
  .tickets { position: absolute; left: 70px; top: 784px; width: 720px; font-size: 17px; line-height: 1.35; }
  .tickets .lead { color: var(--gold); font-size: 22px; line-height: 1.2; }

  .details { position: absolute; left: 70px; top: 886px; display: flex; align-items: flex-start; }
  .details section { font-size: 17px; line-height: 1.35; }
  .details ul { list-style: none; }
  .details li::before { content: "• "; }
  .col-include { width: 222px; padding-right: 10px; }
  .col-drinks { width: 270px; padding-left: 11px; border-left: 1px solid var(--mist); padding-bottom: 26px; }
  .col-djs { padding-left: 11px; border-left: 1px solid var(--mist); }
  .col-djs .heading + ul { margin-bottom: 14px; }

  .brand {
    position: absolute; left: 30px; top: 1020px;
    display: flex; align-items: center; gap: 14px;
    font-weight: 700; font-size: 62px; line-height: 1; color: var(--white);
  }
  .brand-dot { width: 22px; height: 22px; border-radius: 50%; background: var(--white); }

  .contact-band {
    position: absolute; left: 0; bottom: 0; width: 100%; height: 80px;
    background: var(--lime); color: var(--ink);
    font-size: 18px; padding: 36px 0 0 25px; white-space: nowrap;
  }
</style>
</head>
<body>
  <main class="flyer">
    <div class="party-photo" role="img" aria-label="Photo of two party guests in a feathered top hat and a golden masquerade mask"></div>
    <div class="crown-art" role="img" aria-label="Illustration of a golden jewelled crown"></div>

    <h1 class="event-title">
      <span class="title-line-1">Lantern’s</span>
      <span class="title-line-2">Harvest</span>
      <span class="title-line-3">Night</span>
    </h1>
    <p class="tagline">While the Queen’s away<br>the staff will play!</p>

    <p class="intro">While the Queen is out celebrating her birthday with high tea, the palace staff are throwing a party at 14th loftspace and drinking her booze!</p>

    <div class="when">
      <div class="date">JUNE<small>2012</small><br>10<sup>th</sup></div>
      <div class="time">8:00<small>PM</small><br>3:00<small>AM</small></div>
      <div class="dress">Dress code:<strong>Smart/casual</strong>or join in the theme</div>
    </div>

    <div class="tickets">
      <h2 class="heading">Tickets</h2>
      <p class="lead">Purchased through our website or Friendlink page, at the venue or at the door</p>
      <p>Pre-Purchase Tickets: <b>$10</b></p>
      <p>Entry on the night (subject to availability): <b>$15</b></p>
    </div>

    <div class="details">
      <section class="col-include">
        <h2 class="heading">Tickets include:</h2>
        <ul>
          <li>Priority entry</li>
          <li>Finger food from 9-10pm</li>
          <li>‘Kir Royal’ cocktail on arrival</li>
        </ul>
      </section>
      <section class="col-drinks">
        <h2 class="heading">Drink specials:</h2>
        <ul>
          <li>$10 Kir Royal’s all night long!</li>
          <li>$20 Valdoro buckets from 9-11pm</li>
        </ul>
      </section>
      <section class="col-djs">
        <h2 class="heading">DJ’s</h2>
        <ul><li>Playing from 9:00-3:00am</li></ul>
        <h2 class="heading">Line up includes:</h2>
        <ul>
          <li>Dusky Amber</li>
          <li>Tilted</li>
          <li>DJ Marvek</li>
        </ul>
      </section>
    </div>

    <div class="brand"><span>14th loftspace</span><span class="brand-dot"></span></div>

    <footer class="contact-band">Ph: (03) 9514 2760 • Web: www.14thloftspace.com.au • Address: 14 Marlowe Lane St Kilda</footer>
  </main>
</body>
</html>
```